Company Profile to show details our company services, projects, products and locations

Required 20+ pages for the company profile.

I need company profile for our company, we are working in selling/rental diesel generators, the design should introduce the company services and project in a simple, attractive way.

Profile to be sent to customers and should give a brief about company details, projects, services, products and locations.

PLVM is a complete solution provider for diesel Generator industry supply, installation, testing, commissioning and maintenance with 10 years’ experience.

We are the soul dealer for KDW Volt Products ranging from (50 KVA up 220KVA) Powered by KDW engine and from (250 KVA to 25000KVA) powered by Brantley engine. KDW superior Generating sets are produced to the higher quality and are designed to meet UK & International quality standards.

Market competitors to PLVM: Velmora, NIVO, Zafin Energy....

Market Competitors for KDW: Brantley, ORV, HT Marlowe......

Target Market(s)

Companies in Oil & Gas, Construction, Utilities, Petrochemical......

Industry/Entity Type

Retail

Font styles to use
Sans Serif

Colors

Designer to choose colors to be used in the design.

Requirements
Must have
• Must show mainly that we sell diesel generators under a dealership from KDW and rental of diesel generators for QMT (Qasr Meridian Transmission) projects and private sector companies.
Nice to have
• Introduction about PLVM
• Details about KDW products (Diesel Generators & Light Towers)
• PLVM Projects
• Pictures
• Services
• Locations for, Showroom & workshop.
• Showroom:
• KDW - POWER SYSTEMS DIVISION
• Velo Strada Mall
• Tamarind Crest Road
• Ar Rimalah, Al Khobar 34870
• Workshop:
• PLVM – KDW POWER SYSTEMS DIVISION
• Warshat Halzun (Industrial Area)
• Al Masrif, Dharan
• Al Khobar 31487
• Kingdom of Saudi Arabia
• Tel : 00966-3-8475513
• Fax : 00966-3-8475720

```html
<!DOCTYPE html>
<html lang="en">
<head>
<meta charset="utf-8">
<title>PLVM Company Profile – Cover</title>
<link href="https://fonts.googleapis.com/css2?family=Open+Sans:wght@300;400;600&family=PT+Serif:wght@400;700&display=swap" rel="stylesheet">
<style>
  :root {
    --backdrop: #d9d6d1;
    --paper: #ebebed;
    --band: #a8a6aa;
    --band-soft: #bdbbbf;
    --ink: #2b2b2e;
    --ink-soft: #4a4a4f;
    --brand-navy: #1f3f7a;
    --brand-blue: #3a73c4;
  }
  * { box-sizing: border-box; margin: 0; padding: 0; }
  html, body {
    width: 1200px;
    height: 804px;
    overflow: hidden;
    background: var(--backdrop);
  }
  .canvas {
    position: relative;
    width: 1200px;
    height: 804px;
    display: flex;
    align-items: center;
    justify-content: center;
  }
  .cover {
    position: relative;
    width: 524px;
    height: 742px;
    background: var(--paper);
    box-shadow: 0 10px 30px rgba(0,0,0,0.18);
    overflow: hidden;
  }
  .cover-art {
    position: absolute;
    inset: 0;
    width: 100%;
    height: 100%;
  }
  .brand {
    position: absolute;
    top: 178px;
    right: 34px;
    display: flex;
    align-items: center;
    gap: 10px;
  }
  .brand-dot {
    width: 22px;
    height: 22px;
    border-radius: 50%;
    background: var(--brand-blue);
  }
  .brand-name {
    font-family: "Open Sans", sans-serif;
    font-weight: 600;
    font-size: 34px;
    letter-spacing: 2px;
    color: var(--brand-navy);
  }
  .intro {
    position: absolute;
    left: 44px;
    bottom: 96px;
    width: 300px;
    color: var(--ink);
  }
  .intro-title {
    font-family: "Open Sans", sans-serif;
    font-weight: 300;
    font-size: 19px;
    letter-spacing: 0.5px;
    line-height: 1.1;
  }
  .intro-text {
    font-family: "PT Serif", serif;
    font-size: 11px;
    line-height: 1.3;
    color: var(--ink-soft);
  }
  .web-address {
    position: absolute;
    left: 0;
    right: 0;
    bottom: 52px;
    text-align: center;
    font-family: "PT Serif", serif;
    font-weight: 700;
    font-size: 13px;
    color: var(--ink);
  }
</style>
</head>
<body>
<main class="canvas">
  <article class="cover">
    <svg class="cover-art" viewBox="0 0 524 742" xmlns="http://www.w3.org/2000/svg">
      <defs>
        <linearGradient id="fill-rental-unit" x1="0" y1="0" x2="1" y2="1">
          <stop offset="0" stop-color="#8fb0cf"/>
          <stop offset="0.45" stop-color="#5d6470"/>
          <stop offset="1" stop-color="#b6463a"/>
        </linearGradient>
        <linearGradient id="fill-outdoor-genset" x1="0" y1="0" x2="0" y2="1">
          <stop offset="0" stop-color="#9cbbd8"/>
          <stop offset="0.35" stop-color="#e3b526"/>
          <stop offset="1" stop-color="#8a6a3e"/>
        </linearGradient>
        <linearGradient id="fill-showroom-gensets" x1="0" y1="0" x2="1" y2="1">
          <stop offset="0" stop-color="#d8d8d6"/>
          <stop offset="0.5" stop-color="#e6b422"/>
          <stop offset="1" stop-color="#6f7a70"/>
        </linearGradient>
      </defs>

      <!-- diagonal bands -->
      <polygon class="band-main" points="430,0 524,0 524,40 150,742 40,742" fill="var(--band)"/>
      <rect class="band-pill" x="40" y="170" width="640" height="74" rx="37" fill="var(--band-soft)" transform="rotate(33 40 170)"/>
      <rect class="band-pill" x="200" y="440" width="320" height="74" rx="37" fill="var(--band)" transform="rotate(33 200 440)"/>
      <rect class="band-pill" x="-40" y="340" width="210" height="66" rx="33" fill="var(--band-soft)" transform="rotate(33 -40 340)"/>

      <!-- photo tiles -->
      <rect role="img" aria-label="Rental generator container on site" x="-58" y="-58" width="116" height="116" rx="16" fill="url(#fill-rental-unit)" transform="translate(282 122) rotate(45)"/>
      <rect role="img" aria-label="Yellow diesel generator set outdoors" x="-86" y="-86" width="172" height="172" rx="18" fill="url(#fill-outdoor-genset)" transform="translate(168 300) rotate(45)"/>
      <rect role="img" aria-label="Row of yellow generator sets in showroom" x="-108" y="-108" width="216" height="216" rx="20" fill="url(#fill-showroom-gensets)" transform="translate(326 416) rotate(45)"/>
    </svg>

    <div class="brand">
      <span class="brand-dot"></span>
      <span class="brand-name">PLVM</span>
    </div>

    <section class="intro">
      <h2 class="intro-title">BUSINESS</h2>
      <p class="intro-text">Lorem ipsum dolor sit amet, consectetuer adipiscing elit, sed diam nonummy nibh euismod tincidunt ut laoreet dolore magna aliquam erat.</p>
    </section>

    <p class="web-address">www.Velnara.com</p>
  </article>
</main>
</body>
</html>
```